ebook cover for first in a light hearted series of Bright Routine Manuals

My project is a short (8,000 word) ebook The cover needs to include a logo with the words “The Bright Routine Manual”, as this is the first of a series and I want to have a common logo across the different books in the series. The logo also needs to be square so that I can use it as the logo for my podcasts. Something similar to the attached could work, but I am open to ideas:Then, underneath the logo I need the title of the specific book in the series; in this case ‘On Moving With A Partner Abroad’.In addition, I would like a subtitle on the cover saying ‘Easy to Implement Habits to Help You Make the Most of Expat Life.’One or more cover images could be added based on the themes from the chapter headings as below:Chapter Headings are as follows1. Turn up2. Share Your Umbrella3. Do What You Have Always Wanted4. Keep Up and Keep at It5. Use Your Hands6. Pay Attention7. Take The Bus
This is not a traditional self- help book. It features personal stories

Target Market(s)

Expat Women

Font styles to use
Serif
Sans Serif

Colors

Designer to choose colors to be used in the design.

Requirements
Must have
• A warm and whimsical feel
Should not have
• A corporate feel

```html
<!DOCTYPE html>
<html lang="en">
<head>
<meta charset="utf-8">
<title>The Bright Routine Manual – On Moving With A Partner Abroad</title>
<link rel="stylesheet" href="https://fonts.googleapis.com/css2?family=Montserrat:wght@500&family=PT+Sans:wght@400&family=PT+Sans+Narrow:wght@400&display=swap">
<style>
  :root {
    --paper: #ffffff;
    --ink: #0d0d0d;
    --accent-blue: #3b6193;
    --frame-blue: #3f6494;
    --muted-ink: #222222;
  }
  * { margin: 0; padding: 0; box-sizing: border-box; }
  html, body {
    width: 1031px;
    height: 1200px;
    overflow: hidden;
    background: var(--paper);
  }
  .cover {
    position: relative;
    width: 1031px;
    height: 1200px;
    background: var(--paper);
    text-align: center;
    color: var(--ink);
  }
  .cover__subtitle {
    position: absolute;
    top: 140px;
    left: 0;
    right: 0;
    font-family: "Montserrat", sans-serif;
    font-weight: 500;
    font-size: 33px;
    line-height: 1.3;
    color: var(--accent-blue);
  }
  .series-mark {
    position: absolute;
    top: 290px;
    left: 50%;
    transform: translateX(-50%);
    width: 500px;
    height: 500px;
    border: 6px solid var(--frame-blue);
    display: flex;
    flex-direction: column;
    justify-content: center;
    align-items: center;
    font-family: "PT Sans", sans-serif;
    font-weight: 400;
    color: var(--ink);
    line-height: 0.98;
  }
  .series-mark__line { display: block; }
  .series-mark__line--small { font-size: 92px; }
  .series-mark__line--large { font-size: 132px; }
  .cover__title {
    position: absolute;
    top: 812px;
    left: 0;
    right: 0;
    font-family: "PT Sans Narrow", sans-serif;
    font-weight: 400;
    font-size: 60px;
    color: var(--ink);
  }
  .chapter-list {
    position: absolute;
    top: 960px;
    left: 0;
    right: 0;
    font-family: "PT Sans Narrow", sans-serif;
    font-weight: 400;
    font-size: 22px;
    line-height: 1.7;
    color: var(--muted-ink);
    list-style: none;
  }
</style>
</head>
<body>
  <main class="cover">
    <p class="cover__subtitle">Easy to Implement Habits to Help<br>You Make the Most of Expat Life</p>

    <h1 class="series-mark">
      <span class="series-mark__line series-mark__line--small">The Bright</span>
      <span class="series-mark__line series-mark__line--large">Routine</span>
      <span class="series-mark__line series-mark__line--large">Manual</span>
    </h1>

    <h2 class="cover__title">On Moving With A Partner Abroad</h2>

    <ul class="chapter-list">
      <li>follows1 | Turn up2 | Share Your Umbrella3</li>
      <li>Do What You Have Always Wanted4 &nbsp;| Keep Up and Keep at It5</li>
      <li>Use Your Hands6 | Pay Attention7. Take The Bus</li>
    </ul>
  </main>
</body>
</html>
```